Feng Shui Consultant needing a business card designed

please incorporate the following colours in the design: lilac (primarily)black and gold
Name of the business is: Heron Feng Shui
The main design should incorporate a willow tree, to be the main focus of the design
The design should be modern and sophisticated
The back of the card should include the following details;
name; Maribel Costade
title: Accredited Feng Shui Consultant
phone number; 0472 915 384
email address; maribel_costade@quillpost.example
Specialising in Feng Shui and Space Clearing

Highend, affluent white collar clients. Well educated

Business

e3daeb

```html
<!DOCTYPE html>
<html lang="en">
<head>
<meta charset="utf-8">
<title>Heron Feng Shui – Business Card</title>
<link rel="stylesheet" href="https://fonts.googleapis.com/css2?family=Macondo&family=Questrial&display=swap">
<style>
  :root {
    --page: #ffffff;
    --lilac: #e0cbf6;
    --lilac-light: #fbf8ff;
    --ink: #2a2228;
    --ink-soft: #3b3340;
    --gold: #c9a978;
    --gold-light: #eadcc0;
    --bark: #2b2326;
    --shadow: rgba(60, 40, 80, 0.28);
  }
  * { margin: 0; padding: 0; box-sizing: border-box; }
  html, body {
    width: 1010px;
    height: 1200px;
    overflow: hidden;
    background: var(--page);
  }
  .sheet { position: relative; width: 1010px; height: 1200px; }

  .card {
    position: absolute;
    width: 799px;
    height: 472px;
    background: radial-gradient(ellipse 55% 60% at 45% 50%, var(--lilac-light) 0%, var(--lilac) 100%);
    box-shadow: 6px 10px 14px var(--shadow);
  }
  .card--front { left: 109px; top: 64px; }
  .card--back  { left: 103px; top: 605px; }

  .tree-art {
    position: absolute;
    border-radius: 10px;
    background: linear-gradient(180deg, var(--gold-light) 0%, var(--gold) 55%, var(--bark) 100%);
  }
  .card--front .tree-art { left: 258px; top: 40px; width: 276px; height: 300px; }
  .card--back  .tree-art { left: 502px; top: 130px; width: 216px; height: 242px; }

  .brand-name {
    position: absolute;
    left: 0; right: 0;
    top: 346px;
    text-align: center;
    font-family: "Macondo", fantasy;
    font-weight: 400;
    font-size: 58px;
    letter-spacing: 6px;
    color: var(--ink);
  }

  .person-name {
    position: absolute;
    left: 92px; top: 86px;
    font-family: "Macondo", fantasy;
    font-weight: 400;
    font-size: 34px;
    letter-spacing: 1px;
    color: var(--ink);
  }
  .person-title {
    position: absolute;
    left: 92px; top: 144px;
    font-family: "Questrial", sans-serif;
    font-size: 21px;
    color: var(--ink-soft);
  }
  .contact {
    position: absolute;
    left: 92px;
    display: flex;
    align-items: center;
    gap: 6px;
    font-family: "Questrial", sans-serif;
    font-size: 21px;
    color: var(--ink-soft);
  }
  .contact--phone { top: 249px; }
  .contact--email { top: 289px; }
  .contact svg { fill: var(--ink-soft); flex: none; }

  .tagline {
    position: absolute;
    left: 0; right: 0;
    top: 390px;
    text-align: center;
    font-family: "Macondo", fantasy;
    font-size: 32px;
    letter-spacing: 1.5px;
    color: var(--ink);
  }
</style>
</head>
<body>
<main class="sheet">
  <section class="card card--front">
    <div class="tree-art" role="img" aria-label="Willow tree illustration with dark trunk and gold hanging leaves"></div>
    <h1 class="brand-name">Heron Feng Shui</h1>
  </section>

  <section class="card card--back">
    <h2 class="person-name">Maribel Costade</h2>
    <p class="person-title">Accredited Feng Shui Consultant</p>
    <p class="contact contact--phone">
      <svg width="18" height="22" viewBox="0 0 18 22" aria-hidden="true">
        <path d="M4 1 L7 1 L8 6 L6 8 C7 11 9 14 11 15 L13 13 L17 15 L17 18 C17 20 15 21 13 21 C6 19 1 12 1 5 C1 3 2 1 4 1 Z"/>
      </svg>
      0472 915 384
    </p>
    <p class="contact contact--email">
      <svg width="22" height="16" viewBox="0 0 22 16" aria-hidden="true">
        <path d="M1 1 H21 V15 H1 Z M3 3 V13 H19 V3 L11 9 Z M4 3 L11 8 L18 3 Z" fill-rule="evenodd"/>
      </svg>
      maribel_costade@quillpost.example
    </p>
    <div class="tree-art" role="img" aria-label="Willow tree illustration with dark trunk and gold hanging leaves"></div>
    <p class="tagline">Specialising in Feng Shui and Space Clearing</p>
  </section>
</main>
</body>
</html>
```